I would like to modify/update my 2 step login screen

I want a more modern looking login page for our document imaging application. I need to keep all of the same elements and buttons that currently exist. The first 2 screens are the login. The 3rd is a screenshot of the actual application home page.

```html
<!DOCTYPE html>
<html lang="en">
<head>
<meta charset="utf-8">
<title>MRDS Login</title>
<link rel="stylesheet" href="https://fonts.googleapis.com/css2?family=Barlow:wght@400;500;600&family=Montserrat:wght@500;700;800&display=swap">
<style>
  :root {
    --navy-deep: #07152b;
    --navy-mid: #0e2a52;
    --brand-blue: #2f78c4;
    --card-bg: #ffffff;
    --panel-bg: #f6f9fc;
    --field-bg: #f3f6f9;
    --field-border: #d9dee4;
    --ink: #0b1a2e;
    --muted: #3c4756;
    --green: #34a853;
    --orange: #f25022;
    --white: #ffffff;
  }
  * { box-sizing: border-box; margin: 0; padding: 0; }
  html, body { width: 1200px; height: 830px; overflow: hidden; }
  body {
    position: relative;
    background: var(--navy-deep);
    font-family: "Barlow", sans-serif;
    color: var(--ink);
  }
  .city-backdrop {
    position: absolute; inset: 0;
    background: linear-gradient(180deg, #071326 0%, #0b2040 35%, #12315c 60%, #1b3a63 80%, #0f2645 100%);
  }
  .decor { position: absolute; inset: 0; }
  .band-top, .band-bottom { position: absolute; }
  .brand {
    position: absolute; left: 0; right: 0; top: 66px;
    display: flex; justify-content: center; align-items: center; gap: 10px;
  }
  .brand-mark { width: 26px; height: 26px; background: var(--white); border-radius: 4px; }
  .brand-name {
    font-family: "Montserrat", sans-serif; font-weight: 700;
    font-size: 26px; color: var(--white); letter-spacing: 0.5px;
  }
  .page-title {
    position: absolute; left: 0; right: 0; top: 140px;
    text-align: center; font-family: "Montserrat", sans-serif;
    font-weight: 800; font-size: 42px; color: var(--white); letter-spacing: 0.5px;
  }
  .login-card {
    position: absolute; left: 343px; top: 217px; width: 515px; height: 450px;
    background: var(--card-bg); border-radius: 13px; padding: 20px;
  }
  .login-panel {
    width: 100%; height: 100%;
    background: var(--panel-bg); border: 1.5px solid var(--brand-blue);
    border-radius: 13px; padding: 30px 31px 0;
  }
  .field-database {
    display: block; width: 100%; height: 51px;
    background: var(--field-bg); border: 1px solid var(--field-border); border-radius: 5px;
    padding: 0 18px; font-family: "Barlow", sans-serif; font-size: 13px; color: var(--muted);
    line-height: 49px;
  }
  .btn {
    display: flex; align-items: center; justify-content: center; gap: 12px;
    width: 100%; height: 51px; border-radius: 5px; margin-top: 15px;
    font-family: "Barlow", sans-serif; font-weight: 600; font-size: 16px; color: var(--ink);
    background: var(--panel-bg);
  }
  .btn-primary {
    background: var(--brand-blue); color: var(--white);
    font-family: "Montserrat", sans-serif; font-weight: 800; font-size: 13px; letter-spacing: 0.2px;
    margin-top: 15px;
  }
  .btn-northgate { border: 1.5px solid var(--green); margin-top: 15px; }
  .btn-bluepane { border: 1.5px solid var(--orange); margin-top: 9px; }
  .btn-keyring { border: 1.5px solid var(--brand-blue); margin-top: 9px; }
  .provider-dot { width: 13px; height: 13px; border-radius: 50%; background: var(--ink); }
  .provider-square { width: 13px; height: 13px; background: var(--ink); }
  .audit-note {
    margin-top: 17px; text-align: center; font-size: 12px; line-height: 19px; color: var(--muted);
  }
  .site-footer {
    position: absolute; left: 0; right: 0; top: 712px; text-align: center;
    font-family: "Montserrat", sans-serif; font-weight: 500; color: var(--white);
  }
  .footer-links { font-size: 16px; }
  .copyright { font-size: 16px; margin-top: 14px; }
</style>
</head>
<body>
  <div class="city-backdrop" role="img" aria-label="Darkened city skyline photograph in deep blue tones"></div>

  <svg class="decor" width="1200" height="830" viewBox="0 0 1200 830" aria-hidden="true">
    <circle cx="-20" cy="72" r="185" fill="none" stroke="#17325a" stroke-width="5"/>
    <circle cx="1230" cy="780" r="230" fill="none" stroke="#1f3f68" stroke-width="3" opacity="0.7"/>
    <rect x="616" y="0" width="584" height="13" fill="#2f78c4"/>
    <polygon points="557,0 563,0 571,13 565,13" fill="#2f78c4"/>
    <polygon points="570,0 576,0 584,13 578,13" fill="#2f78c4"/>
    <polygon points="583,0 589,0 597,13 591,13" fill="#2f78c4"/>
    <polygon points="596,0 602,0 610,13 604,13" fill="#2f78c4"/>
    <rect x="0" y="816" width="578" height="14" fill="#2f78c4"/>
    <polygon points="584,830 590,830 596,816 590,816" fill="#2f78c4"/>
    <polygon points="597,830 603,830 609,816 603,816" fill="#2f78c4"/>
    <polygon points="610,830 616,830 622,816 616,816" fill="#2f78c4"/>
    <polygon points="623,830 629,830 635,816 629,816" fill="#2f78c4"/>
  </svg>

  <header class="brand">
    <span class="brand-mark"></span>
    <span class="brand-name">MERIDIAN RECORDS</span>
  </header>

  <h1 class="page-title">MRDS LOGIN</h1>

  <main class="login-card">
    <div class="login-panel">
      <div class="field-database">Database</div>
      <div class="btn btn-primary">
        LOG IN WITH MYRECORDVIEW
        <svg width="16" height="12" viewBox="0 0 16 12" aria-hidden="true"><path d="M1 6h13M9 1l5 5-5 5" fill="none" stroke="#fff" stroke-width="1.8" stroke-linecap="round" stroke-linejoin="round"/></svg>
      </div>
      <div class="btn btn-northgate"><span class="provider-dot"></span>Log in with Northgate</div>
      <div class="btn btn-bluepane"><span class="provider-square"></span>Log in with Bluepane</div>
      <div class="btn btn-keyring"><span class="provider-dot"></span>Log in with Keyring</div>
      <p class="audit-note">All activity on this site is being recorded.<br>Your IP Address is being saved as '192.168.168.134</p>
    </div>
  </main>

  <footer class="site-footer">
    <div class="footer-links">Privacy | Remote Support | Contact Us</div>
    <div class="copyright">Copyright © 2024 Meridian Records Co., All rights reserved.</div>
  </footer>
</body>
</html>
```